Thesis cover and chapter page design

I am looking for a PhD thesis cover design with accompanying chapter pages . The chapter pages do not have to be unique designs and can be copies of the cover with small adjustment (for example colour to grey).

The topic of the thesis is ischemic stroke, which is caused by a blood clot in one of the anterior arteries of the brain (for inspiration search for circle of willis/ middle cerebral artery/anterior cerebral vessel occlusion).

The first half of the thesis is about the clot itself (for inspiration search for "ischemic stroke thrombus"), the second half about the ischemic region in the brain measured on MRI/diffusion weighted imaging (for inspiration search for "ischemic stroke ischemic lesion MR").

It would be great if the design contains something creative with my hobby sailing, but this is not neccessary. The design can be abstract, animation type, realistic... just get creative :)

Both back cover and front cover need to be 17 cm with 0.5 cm bleed. The size of the spine is unknown, since it depends on the number of pages. Please, provide me with a photoshop file ( or GIMP if possible).

```html
<!DOCTYPE html>
<html lang="en">
<head>
<meta charset="utf-8">
<title>Thesis cover and chapter pages</title>
<link href="https://fonts.googleapis.com/css2?family=Open+Sans:wght@300;400&family=Arimo:wght@400;700&display=swap" rel="stylesheet">
<style>
  :root {
    --stage: #d9d9d9;
    --cover-deep: #0b0a1f;
    --cover-mid: #1b1660;
    --cover-violet: #3a22c8;
    --brain-glow: #6a8cff;
    --brain-pink: #b24bd6;
    --red-deep: #3e0b0b;
    --red-mid: #7c1a14;
    --red-accent: #d2262c;
    --green-deep: #082a0e;
    --green-mid: #1c6a23;
    --green-accent: #2fae3a;
    --paper: #f7f7f7;
    --ink: #2a2a2a;
    --box: #e2e2e2;
    --white: #ffffff;
  }
  * { box-sizing: border-box; margin: 0; padding: 0; }
  html, body { width: 1200px; height: 933px; overflow: hidden; }
  body { background: var(--stage); position: relative; font-family: "Open Sans", sans-serif; }

  /* ---------- cover wrap ---------- */
  .cover-wrap {
    position: absolute; top: 30px; left: 298px;
    width: 604px; height: 420px;
    display: flex;
    box-shadow: 0 6px 18px rgba(0,0,0,.18);
  }
  .cover-page { position: relative; width: 295px; height: 420px; overflow: hidden; background: var(--cover-deep); }
  .cover-page svg.cover-bg { position: absolute; inset: 0; width: 100%; height: 100%; }
  .spine {
    width: 14px; height: 420px; background: linear-gradient(90deg, #120f3a, #221a70, #120f3a);
    position: relative; overflow: hidden;
  }
  .spine-title {
    position: absolute; top: 210px; left: 7px;
    transform: translate(-50%, -50%) rotate(90deg);
    white-space: nowrap; color: var(--white); font-size: 6px; font-weight: 300; letter-spacing: .2px;
  }
  .brain-art {
    position: absolute; border-radius: 50%;
    background: radial-gradient(ellipse at 45% 45%, rgba(150,180,255,.85) 0%, rgba(106,140,255,.6) 30%, rgba(178,75,214,.35) 55%, rgba(58,34,200,0) 75%);
  }
  .brain-art--front { width: 300px; height: 250px; left: -60px; top: 175px; }
  .brain-art--back { width: 300px; height: 250px; right: -120px; top: 175px; }
  .cover-title {
    position: absolute; top: 34px; right: 18px;
    text-align: right; color: var(--white);
    font-weight: 300; font-size: 20px; line-height: 1.12;
  }

  /* ---------- chapter spreads ---------- */
  .spread {
    position: absolute; top: 485px; width: 566px; height: 400px;
    display: flex; box-shadow: 0 6px 18px rgba(0,0,0,.16);
  }
  .spread--one { left: 19px; }
  .spread--two { left: 615px; }
  .text-page {
    width: 283px; height: 400px; background: var(--paper);
    padding: 30px 20px 24px 24px;
    font-family: "Arimo", sans-serif; color: var(--ink);
    font-size: 6.4px; line-height: 1.42;
    display: flex; flex-direction: column; justify-content: space-between;
    border-right: 1px solid #d6d6d6;
  }
  .text-columns { display: grid; grid-template-columns: 1fr 1fr; gap: 12px; }
  .text-page h3 { font-size: 7px; font-weight: 700; margin-bottom: 4px; }
  .text-page p { margin-bottom: 6px; }
  .text-page h3.mid { margin-top: 4px; }
  .summary-box {
    background: var(--box); padding: 12px 12px 10px;
    display: grid; grid-template-columns: 1fr 1fr; gap: 12px;
  }
  .summary-box ul { padding-left: 9px; }
  .summary-box li { margin-bottom: 3px; }

  .chapter-page { position: relative; width: 283px; height: 400px; overflow: hidden; }
  .chapter-page svg.chapter-bg { position: absolute; inset: 0; width: 100%; height: 100%; }
  .chapter-art {
    position: absolute; width: 230px; height: 190px; left: 20px; top: 130px; border-radius: 50%;
  }
  .chapter-page--red .chapter-art { background: radial-gradient(ellipse, rgba(230,120,100,.45) 0%, rgba(160,50,40,.25) 45%, rgba(124,26,20,0) 72%); }
  .chapter-page--green .chapter-art { background: radial-gradient(ellipse, rgba(140,220,140,.4) 0%, rgba(50,140,60,.22) 45%, rgba(28,106,35,0) 72%); }
  .chapter-heading {
    position: absolute; top: 26px; right: 18px; text-align: right;
    font-weight: 300; font-size: 15px; line-height: 1.1; color: var(--white);
  }
  .chapter-label { display: block; }
  .chapter-page--red .chapter-label { color: var(--red-accent); }
  .chapter-page--green .chapter-label { color: var(--green-accent); }
</style>
</head>
<body>

<section class="cover-wrap">
  <div class="cover-page cover-page--back">
    <svg class="cover-bg" viewBox="0 0 295 420" preserveAspectRatio="none">
      <defs>
        <linearGradient id="backFill" x1="0" y1="0" x2="1" y2="1">
          <stop offset="0" stop-color="#0a0920"/><stop offset=".6" stop-color="#16124d"/><stop offset="1" stop-color="#2a1fa0"/>
        </linearGradient>
      </defs>
      <rect width="295" height="420" fill="url(#backFill)"/>
      <polygon points="150,0 295,0 295,420" fill="#8a6cff" opacity=".12"/>
    </svg>
    <div class="brain-art brain-art--back" role="img" aria-label="Glowing blue and violet brain with vessel lines, continued from the front cover"></div>
  </div>
  <div class="spine"><span class="spine-title">Thrombus and ischemic core in acute ischemic stroke and their relation to functional outcome</span></div>
  <div class="cover-page cover-page--front">
    <svg class="cover-bg" viewBox="0 0 295 420" preserveAspectRatio="none">
      <defs>
        <linearGradient id="frontFill" x1="0" y1="1" x2="1" y2="0">
          <stop offset="0" stop-color="#2f20b8"/><stop offset=".5" stop-color="#1b1660"/><stop offset="1" stop-color="#0b0a1f"/>
        </linearGradient>
      </defs>
      <rect width="295" height="420" fill="url(#frontFill)"/>
      <polygon points="0,0 0,420 210,420" fill="#ffffff" opacity=".06"/>
      <polygon points="0,260 295,150 295,175 0,300" fill="#6a4cff" opacity=".12"/>
    </svg>
    <div class="brain-art brain-art--front" role="img" aria-label="Glowing blue and violet brain with vessel lines on a dark background"></div>
    <h1 class="cover-title">Thrombus and ischemic core<br>in acute ischemic stroke<br>and their relation to<br>functional outcome</h1>
  </div>
</section>

<section class="spread spread--one">
  <article class="text-page">
    <div class="text-columns">
      <div>
        <h3>Met aut ut occum ellectur</h3>
        <p>Clot composition varies between patients and may shape how readily the occlusion responds to treatment in the first hours.</p>
        <p>Imaging before thrombectomy helps estimate clot length, density and position within the middle cerebral artery and its branches.</p>
        <p>Earlier reperfusion tends to limit the growth of the ischemic core and improves the chance of independent living after stroke.</p>
      </div>
      <div>
        <p>Histology of retrieved material shows layers of red cells, fibrin and platelets in different proportions across cases.</p>
        <p>These findings are compared with baseline scans and clinical scores recorded at admission and at ninety days.</p>
        <h3 class="mid">Porat alisimi laborehende latu invero</h3>
        <p>Outcome is measured on the modified Rankin scale and related to both thrombus features and lesion volume.</p>
      </div>
    </div>
    <div class="summary-box">
      <div>
        <h3>Lestint urionemporis quisitatur</h3>
        <p>Key points of this section in brief:</p>
        <ul>
          <li>Clot density on computed tomography</li>
          <li>Lesion volume on diffusion imaging</li>
          <li>Functional outcome after three months</li>
        </ul>
      </div>
      <div><p>Results are discussed in relation to current treatment guidelines and future trial design.</p></div>
    </div>
  </article>
  <article class="chapter-page chapter-page--red">
    <svg class="chapter-bg" viewBox="0 0 283 400" preserveAspectRatio="none">
      <defs>
        <linearGradient id="redFill" x1="0" y1="0" x2="1" y2="1">
          <stop offset="0" stop-color="#6b1a16"/><stop offset=".5" stop-color="#4a0f0d"/><stop offset="1" stop-color="#8a1c12"/>
        </linearGradient>
      </defs>
      <rect width="283" height="400" fill="url(#redFill)"/>
      <polygon points="0,60 283,260 283,400 0,400" fill="#b03a2a" opacity=".35"/>
    </svg>
    <div class="chapter-art" role="img" aria-label="Faint reddish brain image behind the section title"></div>
    <h2 class="chapter-heading"><span class="chapter-label">Section one</span>Ischemic stroke<br>thrombus</h2>
  </article>
</section>

<section class="spread spread--two">
  <article class="text-page">
    <div class="text-columns">
      <div>
        <h3>Met aut ut occum ellectur</h3>
        <p>Clot composition varies between patients and may shape how readily the occlusion responds to treatment in the first hours.</p>
        <p>Imaging before thrombectomy helps estimate clot length, density and position within the middle cerebral artery and its branches.</p>
        <p>Earlier reperfusion tends to limit the growth of the ischemic core and improves the chance of independent living after stroke.</p>
      </div>
      <div>
        <p>Histology of retrieved material shows layers of red cells, fibrin and platelets in different proportions across cases.</p>
        <p>These findings are compared with baseline scans and clinical scores recorded at admission and at ninety days.</p>
        <h3 class="mid">Porat alisimi laborehende latu invero</h3>
        <p>Outcome is measured on the modified Rankin scale and related to both thrombus features and lesion volume.</p>
      </div>
    </div>
    <div class="summary-box">
      <div>
        <h3>Lestint urionemporis quisitatur</h3>
        <p>Key points of this section in brief:</p>
        <ul>
          <li>Clot density on computed tomography</li>
          <li>Lesion volume on diffusion imaging</li>
          <li>Functional outcome after three months</li>
        </ul>
      </div>
      <div><p>Results are discussed in relation to current treatment guidelines and future trial design.</p></div>
    </div>
  </article>
  <article class="chapter-page chapter-page--green">
    <svg class="chapter-bg" viewBox="0 0 283 400" preserveAspectRatio="none">
      <defs>
        <linearGradient id="greenFill" x1="0" y1="0" x2="1" y2="1">
          <stop offset="0" stop-color="#1f5a24"/><stop offset=".5" stop-color="#0d3512"/><stop offset="1" stop-color="#0a2a0d"/>
        </linearGradient>
      </defs>
      <rect width="283" height="400" fill="url(#greenFill)"/>
      <polygon points="0,60 283,260 283,400 0,400" fill="#2a8a32" opacity=".35"/>
    </svg>
    <div class="chapter-art" role="img" aria-label="Faint green brain image behind the section title"></div>
    <h2 class="chapter-heading"><span class="chapter-label">Section two</span>Ischemic lesion</h2>
  </article>
</section>

</body>
</html>
```